Poster Design Needed for Events

I would like a poster designed for our events.. We do evenings of Mediumship/Psychic at theatres ect.. the image below would need to be included... I Would also like the following wording to be included... "Renowned Spiritualist Medium Dewi Carlow Presents Whispers From The Lantern" There will also Need to be a Place on the poster where event details can be put.. as they Change everytime.. Colours for background maybe blue,, maybe Clouds ect..

```html
<!DOCTYPE html>
<html lang="en">
<head>
<meta charset="utf-8">
<title>Dewi Carlow – Whispers From The Lantern</title>
<link rel="stylesheet" href="https://fonts.googleapis.com/css2?family=Raleway:wght@300&family=Oswald:wght@600&family=Roboto:wght@400&display=swap">
<style>
  :root {
    --sky-deep: #2f6fb8;
    --sky-mid: #5d9ad6;
    --sky-light: #bcd8f0;
    --sun: #ffffff;
    --title-white: #ffffff;
    --accent-yellow: #fff200;
    --info-ink: #1f2b3a;
    --suit-navy: #1c1f33;
    --shirt: #eef1f6;
  }
  * { margin: 0; padding: 0; box-sizing: border-box; }
  html, body { width: 1200px; height: 800px; overflow: hidden; }
  body { background: var(--sky-deep); }

  .poster {
    position: relative;
    width: 1200px;
    height: 800px;
    overflow: hidden;
  }

  .sky-backdrop {
    position: absolute;
    inset: 0;
    background:
      radial-gradient(circle at 255px 225px, var(--sun) 0, rgba(255,255,255,.85) 60px, rgba(220,238,255,.45) 170px, rgba(255,255,255,0) 330px),
      radial-gradient(ellipse at 120px 650px, rgba(235,243,252,.8) 0, rgba(235,243,252,0) 260px),
      radial-gradient(ellipse at 1110px 230px, rgba(235,243,252,.7) 0, rgba(235,243,252,0) 180px),
      radial-gradient(ellipse at 900px 700px, rgba(220,232,245,.55) 0, rgba(220,232,245,0) 280px),
      linear-gradient(170deg, var(--sky-mid) 0%, var(--sky-deep) 45%, #4f8ccb 100%);
  }

  .medium-ghost {
    position: absolute;
    left: 640px;
    top: 90px;
    width: 460px;
    height: 710px;
    border-radius: 220px 220px 0 0;
    background: linear-gradient(180deg, rgba(200,200,210,.18), rgba(30,40,70,.28));
  }

  .medium-portrait {
    position: absolute;
    left: 265px;
    top: 150px;
    width: 375px;
    height: 650px;
    border-radius: 150px 150px 0 0;
    background:
      linear-gradient(180deg, #c9a48f 0%, #b58e7a 30%, var(--shirt) 34%, var(--shirt) 42%, var(--suit-navy) 46%, var(--suit-navy) 100%);
  }

  .headline {
    position: absolute;
    left: 632px;
    top: 112px;
    font-family: "Raleway", sans-serif;
    font-weight: 300;
    color: var(--title-white);
  }
  .headline__line {
    display: block;
    font-size: 52px;
    line-height: 74px;
    letter-spacing: 1px;
  }
  .headline__name {
    display: block;
    font-family: "Oswald", sans-serif;
    font-weight: 600;
    color: var(--accent-yellow);
    font-size: 44px;
    line-height: 60px;
    letter-spacing: 1px;
  }
  .headline__presents {
    display: block;
    font-size: 46px;
    line-height: 76px;
    letter-spacing: 12px;
  }
  .headline__title {
    display: block;
    font-family: "Oswald", sans-serif;
    font-weight: 600;
    color: var(--accent-yellow);
    font-size: 54px;
    line-height: 64px;
    letter-spacing: 0;
  }

  .rule {
    position: absolute;
    height: 2px;
    background: var(--title-white);
  }
  .rule--top { left: 395px; top: 145px; width: 225px; }
  .rule--presents { left: 972px; top: 425px; width: 228px; }
  .rule--bottom { left: 632px; top: 624px; width: 408px; }

  .event-details {
    position: absolute;
    left: 10px;
    top: 562px;
    width: 262px;
    text-align: center;
    font-family: "Roboto", sans-serif;
    color: var(--info-ink);
  }
  .event-details__label {
    font-size: 19px;
    letter-spacing: 1px;
    line-height: 24px;
  }
  .event-details__value {
    font-size: 11px;
    line-height: 15px;
    margin: 4px 0 22px;
  }
</style>
</head>
<body>
  <main class="poster">
    <div class="sky-backdrop" role="img" aria-label="Bright blue sky with white clouds and sunlight bursting behind the medium"></div>
    <div class="medium-ghost" role="img" aria-label="Faint enlarged overlay of the medium fading into the clouds"></div>
    <div class="medium-portrait" role="img" aria-label="Photograph of medium Dewi Carlow in a dark jacket and white shirt, reaching a hand toward the viewer"></div>

    <div class="rule rule--top"></div>
    <div class="rule rule--presents"></div>
    <div class="rule rule--bottom"></div>

    <h1 class="headline">
      <span class="headline__line">RENOWNED</span>
      <span class="headline__line">SPIRITUALIST</span>
      <span class="headline__line">MEDIUM</span>
      <span class="headline__name">DEWI CARLOW</span>
      <span class="headline__presents">PRESENTS</span>
      <span class="headline__title">WHISPERS FROM</span>
      <span class="headline__title">THE LANTERN</span>
    </h1>

    <section class="event-details">
      <h2 class="event-details__label">VENUE</h2>
      <p class="event-details__value">#154, Lorem Ipsum is simply dummy<br>text of the printing and 1542512 industry. 56452</p>
      <h2 class="event-details__label">DATE</h2>
      <p class="event-details__value">21 . 02 . 216</p>
      <h2 class="event-details__label">TIME</h2>
      <p class="event-details__value">10 Am to 1PM</p>
    </section>
  </main>
</body>
</html>
```